Psychotherapy, Life Coaching, Writer, Motivational Speaker

I am a psychotherapist, life coach, writer and speaker on health and wellness issues. I am a humanist - who believes that we are born to self-actualize - but life - changes that course. That we develop armor and coping mechanisms that divert our growth. I help people examine their road blocks to happiness. My business is unique in that I do concierge therapy. I work intensively - with multi-day sessions, I work internationally through tele-therapy - and traditionally - in an office space. My work is tailored to your needs.

Target Market(s)

Broad

Industry/Entity Type

Health

Contact Information for Business Card

Listen And Mend
Tim Harwell
482 East 29th Avenue
New York, NY 10027
(305) 555-0187

Requirements
Must have
• Clean lines... not too busy...
• FB page listing: Listen And Mend
• my Web page: www.listenandmend.example
Nice to have
• I would love to be able to list the services: Psychotherapist, Life Coach, Motivational Speaker and Writer - but also don't want a crazy crowded card. Feel free to use the back for description.
Should not have
• Stay away from corny imagery - lotus flowers, zen, lily pond, clouds.

```html
<!DOCTYPE html>
<html lang="en">
<head>
<meta charset="utf-8">
<title>Listen And Mend — Business Card</title>
<link rel="stylesheet" href="https://fonts.googleapis.com/css2?family=Lato:wght@400;700;900&family=Ubuntu:wght@500&display=swap">
<style>
  :root {
    --canvas: #e6e7ea;
    --brand-blue: #4a82c4;
    --card-white: #ffffff;
    --ink: #1b1b1f;
    --ink-soft: #2a2d3a;
  }
  * { box-sizing: border-box; margin: 0; padding: 0; }
  html, body { width: 1200px; height: 800px; overflow: hidden; }
  body {
    background: var(--canvas);
    font-family: "Lato", Arial, sans-serif;
    color: var(--ink);
    position: relative;
  }
  .card {
    position: absolute;
    width: 520px;
    height: 300px;
    border-radius: 22px;
    top: 250px;
    box-shadow: 0 6px 18px rgba(0,0,0,0.12);
  }
  /* Back side */
  .card-back {
    left: 50px;
    background: var(--brand-blue);
    display: flex;
    flex-direction: column;
    align-items: center;
    justify-content: center;
    text-align: center;
  }
  .back-title {
    font-family: "Lato", Arial, sans-serif;
    font-weight: 900;
    font-size: 24px;
    color: var(--ink);
  }
  .back-services {
    margin-top: 12px;
    font-size: 15px;
    color: var(--ink);
  }
  .back-appointment {
    margin-top: 34px;
    font-size: 15px;
    color: var(--ink);
    letter-spacing: 0.2px;
  }
  /* Front side */
  .card-front {
    left: 630px;
    background: var(--card-white);
    padding: 34px 40px;
  }
  .front-title {
    font-family: "Ubuntu", Arial, sans-serif;
    font-weight: 500;
    font-size: 44px;
    line-height: 1;
    color: var(--brand-blue);
    letter-spacing: -0.5px;
  }
  .front-person {
    margin-top: 28px;
    margin-left: 58px;
  }
  .person-name {
    font-weight: 700;
    font-size: 19px;
    color: var(--brand-blue);
  }
  .person-credentials {
    font-size: 16px;
    color: var(--ink);
  }
  .person-role {
    font-size: 15px;
    color: var(--ink);
    margin-top: 2px;
  }
  .contact-list {
    list-style: none;
    margin-top: 22px;
    margin-left: 58px;
  }
  .contact-item {
    display: flex;
    align-items: center;
    gap: 6px;
    font-size: 16px;
    line-height: 21px;
    color: var(--ink-soft);
  }
  .contact-icon { width: 13px; height: 13px; flex: none; }
  .contact-icon .fill { fill: var(--brand-blue); }
  .contact-icon .line { fill: none; stroke: var(--brand-blue); stroke-width: 1.4; }
</style>
</head>
<body>
  <section class="card card-back" aria-label="Card back">
    <h2 class="back-title">Listen And Mend</h2>
    <p class="back-services">Psychotherapy, Coaching, Wellness Media</p>
    <p class="back-appointment">Your Next Appointment is at.................. at.......... am/pm</p>
  </section>

  <section class="card card-front" aria-label="Card front">
    <h1 class="front-title">Listen And Mend</h1>
    <div class="front-person">
      <p><span class="person-name">Tim Harwell,</span> <span class="person-credentials">LMHC, NCC</span></p>
      <p class="person-role">Psychotherapist.</p>
    </div>
    <ul class="contact-list">
      <li class="contact-item">
        <svg class="contact-icon" viewBox="0 0 14 14" aria-hidden="true">
          <path class="fill" d="M1 5 Q7 0 13 5 L11.5 6.5 L9.5 5.5 L9.5 4.5 Q7 3.5 4.5 4.5 L4.5 5.5 L2.5 6.5 Z"/>
          <rect class="fill" x="3" y="7.5" width="8" height="5" rx="1"/>
        </svg>
        (305) 555-0187
      </li>
      <li class="contact-item">
        <svg class="contact-icon" viewBox="0 0 14 14" aria-hidden="true">
          <rect class="fill" x="0.5" y="2.5" width="13" height="9" rx="1"/>
          <path d="M1 3 L7 8 L13 3 M1 11 L5.5 6.8 M13 11 L8.5 6.8" fill="none" stroke="#fff" stroke-width="1.1"/>
        </svg>
        tharwellcare@example.com
      </li>
      <li class="contact-item">
        <svg class="contact-icon" viewBox="0 0 14 14" aria-hidden="true">
          <circle class="line" cx="7" cy="7" r="6"/>
          <ellipse class="line" cx="7" cy="7" rx="2.6" ry="6"/>
          <path class="line" d="M1 7 H13 M2 4 H12 M2 10 H12"/>
        </svg>
        www.listenandmend.example
      </li>
      <li class="contact-item">
        <svg class="contact-icon" viewBox="0 0 14 14" aria-hidden="true">
          <rect class="fill" x="0.5" y="0.5" width="13" height="13" rx="2"/>
        </svg>
        Listen And Mend
      </li>
    </ul>
  </section>
</body>
</html>
```